THE SALT ORCHARD - "Trade" size book cover design for a novel

THE SALT ORCHARD is a thriller that explores what happens at THE SALT ORCHARD life and death. I'd like to see a cover that reflects the near death experience scenes, but I am open to any creative cover that reflects the theme of the book and the sample scenes that I have attached. Please read the scenes.
Space should be left on the cover for the typical promotional text, etc.

NOVEL SUMMARY - Dr. Dorian Fellwick is skeptical of the afterlife. He doesn't believe he will be reunited with his wife, or joined with God in heaven. What he knows, or thinks he knows, is that he should have seen the warning signs of his wife's heart attack, should have saved her. After four years of mourning, Dorian is finally moving on, succumbing to lust and longing, instead of sorrow. Still he fears the little mistakes that can kill, like a missed diagnosis, or the slip of a scalpel -- the kind of mistakes that depression feeds. When he dates the mother of an epileptic patient, he begins to believe that death will finally stop controlling his life. He has no idea, that the woman of his desires has killed her first husband, and will soon kill her son. As Dorian falls in love and marries, he also becomes involved in a clinical study of near death experiences. Life and research are about to collide.
Updates

The designs I have seen so far are quite dark and seem like they would better fit a horror novel. I am looking for something that is more beautiful. The near death experience scenes in the book are hopeful and wonderous. I also would prefer not to have a dark tunnel representing near death. Moths can also be beautiful creatures. I attached scenes from the book in the original post that might be helpful.

You don't have to use the moth as the focal point, or you might want to use moths as they appear in the main near death scene. I am not wedded to that idea.

Here are some additional ideas for designs: 1. At the climax of the book, there is a scene (see attachment) where there is a fight, and the main character's wife tries to kill him. In that scene, the main character breaks a picture frame with a Hercules Moth specimen over his wife's head. Perhaps a design could incorporate broken glass on the floor with the moth, in whole or part. It could even have a woman's foot wearing and athletic or bicycle shoe stepping on the glass. 2. In the scene where the main character has a near death experience (see attachment), there are vivid surreal descriptions of what he sees, including fluttering moths, numbers and colors. There are also visions of other souls represented as points of light. If this can be represented kind of like a representation of curvatures in space time, all the better. 3. When the main character is a boy, he is slightly autistic and is mesmerized by counting the leaves within a forest tall trees. That could be one possibility for a background. 4. When the main character and wife or on a bicycle vacation in Tuscany, they come across a vineyard after it rains. At the end of one of the vineyard rows, there is a beautiful multicolor rose bush. With droplets of water clinging to the petals. Perhaps there can be reflections in the water drops of moths, or something else (even if it is just light.)

Target Market(s)

Book Readers - Thrillers, suspense, near death experiences, medical(neurology).

Colors

Designer to choose colors to be used in the design.

Requirements
Must have
• Creative design that fits the theme of book. It should not be too dark and brooding (it is not a horror story.) It also should not look like a romance cover.
Nice to have
• One or more of the following as reflected in the attached scenes - Moths, (including Hercules moth); a silhouette of a middle aged bald man perhaps floating in the clouds, shards of broken glass from the picture frame in the climatic scene (not tempered glass from a windshield), near death graphics (not a dark tunnel), time/space or theoretical inspired graphic , the feeling of being caught between two worlds, tree canopy with lots of leaves; enlarged crystaline snow flakes each incorporating a symbol (such a pi, a circle with concentric octagons --ancient method of calculating area of circle, representations or pictures of moths, the symbol for infinity, shards of broken glass, prime numbers, bubbles of color. I am also not opposed to other abstract ideas.
Should not have
• Dark tunnels to represent near death.
• Romance novel cover or overly romantic.
• Horror type novel.

```html
<!DOCTYPE html>
<html lang="en">
<head>
<meta charset="utf-8">
<title>The Salt Orchard — Cover Spread</title>
<link rel="stylesheet" href="https://fonts.googleapis.com/css2?family=Cinzel:wght@400;500&family=EB+Garamond&display=swap">
<style>
  :root {
    --page: #ffffff;
    --stage: #f4f4f4;
    --ink: #1a1a1a;
    --title-ink: #141414;
    --fade-light: #c9c9c9;
    --smoke-deep: #1f2a36;
    --smoke-mid: #5e7183;
    --smoke-pale: #cdd7df;
  }
  * { box-sizing: border-box; margin: 0; padding: 0; }
  html, body {
    width: 899px; height: 1200px; overflow: hidden;
    background: var(--stage);
  }
  .spread {
    position: absolute; left: 0; top: 296px;
    width: 899px; height: 608px;
    background: var(--page);
  }
  .back-blurb {
    position: absolute; left: 32px; top: 48px; width: 352px;
    font-family: "EB Garamond", Georgia, serif;
    font-size: 12.6px; line-height: 18.4px; color: var(--ink);
    text-align: justify; hyphens: auto;
  }
  .spine-title, .spine-author {
    position: absolute; writing-mode: vertical-rl;
    font-family: "Cinzel", "Times New Roman", serif;
    color: var(--ink); font-size: 18px;
  }
  .spine-title { left: 433px; top: 62px; letter-spacing: 1px; }
  .spine-author { left: 435px; top: 370px; font-size: 14px; letter-spacing: 6px; }
  .front-title {
    position: absolute; left: 500px; top: 38px; width: 368px;
    font-family: "Cinzel", "Times New Roman", serif; text-align: right;
  }
  .front-title .line-top {
    display: block; font-size: 42px; line-height: 46px; color: var(--title-ink);
    letter-spacing: 0.5px;
  }
  .front-title .rule {
    display: block; height: 2px; background: var(--title-ink); margin: 4px 0 4px 4px;
  }
  .front-title .line-bottom {
    display: block; font-size: 46px; line-height: 48px; letter-spacing: 1px;
    background: linear-gradient(90deg, #1b1b1b 0%, #6e6e6e 55%, var(--fade-light) 100%);
    -webkit-background-clip: text; background-clip: text; color: transparent;
  }
  .cover-art {
    position: absolute; left: 468px; top: 140px; width: 350px; height: 440px;
    background:
      radial-gradient(ellipse 34% 30% at 40% 22%, var(--smoke-deep) 0%, var(--smoke-mid) 55%, transparent 100%),
      radial-gradient(ellipse 55% 40% at 45% 78%, var(--smoke-mid) 0%, var(--smoke-pale) 60%, transparent 100%),
      radial-gradient(ellipse 12% 10% at 84% 18%, var(--smoke-mid) 0%, transparent 100%),
      radial-gradient(ellipse 60% 55% at 45% 50%, var(--smoke-pale) 0%, transparent 100%);
  }
  .front-author {
    position: absolute; left: 500px; top: 514px; width: 364px; text-align: right;
    font-family: "Cinzel", "Times New Roman", serif; font-size: 36px;
    color: var(--page); letter-spacing: 1px;
    text-shadow: 0 1px 3px rgba(0,0,0,0.55);
  }
</style>
</head>
<body>
  <main class="spread">
    <p class="back-blurb">Dr. Dorian Fellwick is skeptical of the afterlife. He doesn't believe he will be reunited with his wife, or joined with God in heaven. What he knows, or thinks he knows, is that he should have seen the warning signs of his wife's heart attack, should have saved her. After four years of mourning, Dorian is finally moving on, succumbing to lust and longing, instead of sorrow. Still he fears the little mistakes that can kill, like a missed diagnosis, or the slip of a scalpel -- the kind of mistakes that depression feeds. When he dates the mother of an epileptic patient, he begins to believe that death will finally stop controlling his life. He has no idea, that the woman of his desires has killed her first husband, and will soon kill her son. As Dorian falls in love and marries, he also becomes involved in a clinical study of near death experiences. Life and research are about to collide.</p>

    <div class="spine-title">THE SALT ORCHARD</div>
    <div class="spine-author">AUTHOR NAME</div>

    <h1 class="front-title">
      <span class="line-top">THE SALT</span>
      <span class="rule"></span>
      <span class="line-bottom">ORCHARD</span>
    </h1>

    <div class="cover-art" role="img" aria-label="Smoky blue-grey double-exposure portrait of a figure with a dark moth over the chest, fading into white"></div>

    <div class="front-author">AUTHOR NAME</div>
  </main>
</body>
</html>
```